Website Update for Global Company - Solar Technology - Brisqell

We recently released our first version of our website kelvaris.com. However despite a longer process of developing the page, it is still missing the elements of a brilliant website. (Currently it looks dead and boring) We are having problems integrating our logo and want to create a more catching site. The task involves an updated and without changing most of main elements in the existing page. (Unless you can do it even better) The blue color needs to be kept but can be changed within the blue-spectrum. The logo text (KELVARIS) must be better integrated in the site, however the main logo could be used in elements like we have tried with the background. The surface of the logo could be changed to 3D or metallic, or any other theme that would make the site more complete.
It would be good if some elements of the site could be used on business cards and invoices to keep the company identity.
Kelvaris is a new development company specialized in green energy and sustainable development. We do design, engineering, manufacturing, sourcing and other processes related to product development – both as consultants and for own products.
Keep the look of the site as professional as possible, and with a cooperate-looking style.

Link to existing page: www.kelvaris.com

Brief Update : After reviewing the designs we would like all new and current designers to make more bold designs that stands out from the rest. We do not like the standard layout that looks like any other cooperate homepage. We want a very unique and very lively page - with faded images and effects when hoovering like seen on our existing page. Try make all elements blend together, and use faded background images instead of just white color - or something else.

Make the site unique !

Industry/Entity Type

Solar Energy

Contact Information for Business Card

Owner/Founder/CEO : Frederik Lysgaard Holm
Company name: Kelvaris ApS
Email: frederik.lysgaard@kelvaris.dk
Phone: +45 71 83 96 54
Slogan Sustainable Development
Address: Havnestien 18, 2
DK-5820 Svendborg, Denmark

Number of Pages Required

3 page

Font styles to use
Serif
Sans Serif

Colors
0555a3
85acd3
cedeed
3176b5
cee9f5
85cae6
0293ce
86cfc6
33b8a4

```html
<!DOCTYPE html>
<html lang="en">
<head>
<meta charset="utf-8">
<title>Kelvaris – Design, Engineering, Sourcing, Manufacturing</title>
<link href="https://fonts.googleapis.com/css2?family=Roboto:wght@300;400;500;700&family=Roboto+Slab:wght@400;700&display=swap" rel="stylesheet">
<style>
:root{
  --blue-deep:#0555a3;
  --blue-mid:#3176b5;
  --blue-soft:#85acd3;
  --blue-pale:#cedeed;
  --sky:#cee9f5;
  --cyan:#0293ce;
  --grey-bg:#e9ecef;
  --navy:#0b1a2c;
  --ink:#2b3642;
  --white:#ffffff;
}
*{margin:0;padding:0;box-sizing:border-box}
html,body{width:1200px;height:2632px;overflow:hidden}
body{font-family:"Roboto",Arial,sans-serif;color:var(--ink);background:var(--grey-bg);position:relative}
.site-header{height:184px;background:linear-gradient(#f6f7f9,#e6e9ed);position:relative}
.brand{position:absolute;left:0;right:0;top:24px;display:flex;justify-content:center;align-items:center;gap:14px}
.brand-mark{width:44px;height:44px;background:var(--blue-deep)}
.brand-name{font-size:42px;font-weight:500;letter-spacing:3px;color:var(--blue-deep)}
.header-phone{position:absolute;right:40px;top:30px;font-size:16px;color:var(--blue-deep);display:flex;align-items:center;gap:8px}
.main-nav{position:absolute;left:0;right:0;top:126px;display:flex;justify-content:center;gap:6px}
.main-nav a{font-size:13px;text-transform:uppercase;color:var(--ink);text-decoration:none;padding:16px 18px;letter-spacing:.5px}
.main-nav a.active{background:var(--blue-deep);color:var(--white)}
.hero{position:relative;height:556px;overflow:hidden}
.hero-photo{position:absolute;inset:0;background:linear-gradient(180deg,#8fb3d2 0%,#c5d6e4 38%,#7f9aa7 55%,#3f5a6a 75%,#5a7a3e 100%)}
.hero-shade{position:absolute;inset:0;background:linear-gradient(180deg,rgba(0,0,0,0) 30%,rgba(10,30,50,.45) 100%)}
.hero-copy{position:absolute;left:0;right:0;top:300px;text-align:center;color:var(--white)}
.hero-copy h1{font-family:"Roboto Slab",Georgia,serif;font-weight:700;font-size:42px}
.hero-copy p{font-size:28px;font-weight:300;margin:20px auto 0;width:620px;line-height:1.3}
.btn{display:inline-block;margin-top:34px;background:var(--blue-deep);color:var(--white);font-size:20px;padding:16px 40px;text-decoration:none}
.videos{height:408px;position:relative;background:var(--grey-bg)}
.video-card{position:absolute;left:280px;top:80px;width:640px;height:276px;background:linear-gradient(135deg,#b9c2cc,#7d8a97 60%,#5f6b78)}
.video-card .play{position:absolute;left:282px;top:100px}
.video-card h2{position:absolute;left:0;right:0;bottom:40px;text-align:center;color:var(--white);font-size:26px;font-weight:700;letter-spacing:1px}
.news-band{height:132px;background:var(--blue-mid);color:var(--white);text-align:center}
.news-band h2{font-family:"Roboto Slab",Georgia,serif;font-size:34px;padding-top:22px}
.news-list{display:flex;justify-content:center;gap:60px;list-style:none;margin-top:18px;font-size:14px}
.news-list li::before{content:"•";margin-right:10px}
.slider{position:relative;height:440px;overflow:hidden}
.slider-photo{position:absolute;inset:0;background:radial-gradient(ellipse at 55% 45%,#5a4b86 0%,#2a2f55 35%,#c9ccd2 70%,#e4e6ea 100%)}
.slider-copy{position:absolute;left:0;right:0;top:232px;text-align:center;color:var(--white)}
.slider-copy h3{font-size:34px;font-weight:700}
.slider-copy p{font-size:16px;margin-top:8px;line-height:1.4}
.arrow{position:absolute;top:200px}
.arrow.left{left:36px}.arrow.right{right:36px}
.work{height:720px;background:linear-gradient(var(--blue-pale),#b9d0e6);position:relative}
.work h2{text-align:center;font-family:"Roboto Slab",Georgia,serif;color:var(--white);font-size:36px;font-weight:400;padding-top:70px}
.work-grid{position:absolute;left:208px;top:140px;display:grid;grid-template-columns:repeat(3,248px);column-gap:20px;row-gap:56px}
.tile{height:144px;position:relative;overflow:hidden}
.tile .img{position:absolute;inset:0}
.tile span{position:absolute;left:0;right:0;bottom:0;height:36px;line-height:36px;text-align:center;background:var(--blue-mid);color:var(--white);font-size:15px}
.tile.feature .img{background:var(--blue-mid)}
.tile.feature span{background:none;top:0;height:auto;line-height:144px;font-size:22px}
.site-footer{position:absolute;left:0;right:0;bottom:0;height:192px;background:var(--navy);text-align:center}
.socials{display:flex;justify-content:center;gap:18px;padding-top:40px}
.socials i{display:block;width:34px;height:34px;border:2px solid var(--blue-soft);border-radius:50%}
.footer-nav{margin-top:26px;font-size:12px;color:var(--blue-soft);display:flex;justify-content:center;gap:28px}
.copyright{margin-top:14px;font-size:11px;color:#7b8a9a}
.to-top{position:absolute;right:190px;top:46px}
</style>
</head>
<body>
<header class="site-header">
  <div class="brand"><span class="brand-mark"></span><span class="brand-name">KELVARIS</span></div>
  <div class="header-phone">
    <svg width="16" height="16" viewBox="0 0 24 24"><path fill="#0555a3" d="M6.6 10.8a15 15 0 0 0 6.6 6.6l2.2-2.2a1 1 0 0 1 1-.25 11.4 11.4 0 0 0 3.6.6 1 1 0 0 1 1 1V20a1 1 0 0 1-1 1A17 17 0 0 1 3 4a1 1 0 0 1 1-1h3.5a1 1 0 0 1 1 1c0 1.25.2 2.45.6 3.6a1 1 0 0 1-.25 1z"/></svg>
    +45 71 83 96 54
  </div>
  <nav class="main-nav">
    <a class="active" href="#">Home</a><a href="#">Experience</a><a href="#">Approach</a><a href="#">Videos</a><a href="#">About</a><a href="#">Contact Us</a>
  </nav>
</header>

<section class="hero">
  <div class="hero-photo" role="img" aria-label="Wind turbines on green hills behind rows of solar panels under a cloudy sky"></div>
  <div class="hero-shade"></div>
  <div class="hero-copy">
    <h1>Design + Engineering + Sourcing + Manufacturing</h1>
    <p>We provide complete services throughout the product development process</p>
    <a class="btn" href="#">Explore More</a>
  </div>
</section>

<section class="videos">
  <div class="video-card" role="img" aria-label="Hand touching a glowing network of connected nodes">
    <svg class="play" width="76" height="56" viewBox="0 0 76 56"><rect width="76" height="56" rx="12" fill="#ffffff" opacity=".9"/><path d="M30 16v24l20-12z" fill="#6d7885"/></svg>
    <h2>PROJECT VIDEOS</h2>
  </div>
</section>

<section class="news-band">
  <h2>In The News</h2>
  <ul class="news-list">
    <li>Launch of website</li><li>First product released</li><li>Establishment of Kelvaris ApS</li>
  </ul>
</section>

<section class="slider">
  <div class="slider-photo" role="img" aria-label="Tablet computer with a colourful home screen lying at an angle"></div>
  <svg class="arrow left" width="24" height="40" viewBox="0 0 24 40"><path d="M20 4 4 20l16 16" stroke="#fff" stroke-width="4" fill="none"/></svg>
  <svg class="arrow right" width="24" height="40" viewBox="0 0 24 40"><path d="M4 4l16 16L4 36" stroke="#fff" stroke-width="4" fill="none"/></svg>
  <div class="slider-copy">
    <h3>Featured Innovation</h3>
    <p>Kelvaris<br>A family of Tablets + Diverse Individuals</p>
  </div>
</section>

<section class="work">
  <h2>Our Work</h2>
  <div class="work-grid">
    <div class="tile"><div class="img" role="img" aria-label="Engineers at a lab workbench" style="background:linear-gradient(135deg,#d6dde3,#7c8b98)"></div><span>Focused Innovation</span></div>
    <div class="tile feature"><div class="img"></div><span>Industrial Design</span></div>
    <div class="tile"><div class="img" role="img" aria-label="Machined metal parts" style="background:linear-gradient(135deg,#e2e4e6,#5d6268)"></div><span>Working Space Cutting Edge</span></div>
    <div class="tile"><div class="img" role="img" aria-label="Technician working on machinery" style="background:linear-gradient(135deg,#3a5f9a,#c49a62)"></div><span>Mechanical Engineering</span></div>
    <div class="tile"><div class="img" role="img" aria-label="Close-up of a circuit board" style="background:linear-gradient(135deg,#0f6f74,#1d3a4a)"></div><span>Gadgets &amp; Technology</span></div>
    <div class="tile"><div class="img" role="img" aria-label="Colourful electrical wiring" style="background:linear-gradient(135deg,#2c4aa0,#e0c030)"></div><span>Electrical Engineering</span></div>
    <div class="tile"><div class="img" role="img" aria-label="Prototype components on a desk" style="background:linear-gradient(135deg,#c9c4bb,#6c6a66)"></div><span>Prototyping Development</span></div>
    <div class="tile"><div class="img" role="img" aria-label="Factory production line" style="background:linear-gradient(135deg,#8aa6c0,#3f5f7f)"></div><span>Manufacturing Development</span></div>
    <div class="tile"><div class="img" role="img" aria-label="Sketch of a new product concept" style="background:linear-gradient(135deg,#f1f1f1,#a9adb2)"></div><span>New Problem To Solve</span></div>
  </div>
</section>

<footer class="site-footer">
  <div class="socials"><i></i><i></i><i></i><i></i><i></i></div>
  <svg class="to-top" width="20" height="14" viewBox="0 0 20 14"><path d="M2 12 10 4l8 8" stroke="#85acd3" stroke-width="2.5" fill="none"/></svg>
  <div class="footer-nav"><span>Home</span><span>Privacy Policy</span><span>Terms &amp; Conditions</span></div>
  <p class="copyright">Copyright © Kelvaris ApS. All rights reserved. Havnestien 18, 2 DK-5820</p>
</footer>
</body>
</html>
```